Business Card - connecting 2 souls and beggining the journey of self discovery

Logo on the front
with tag line

On the back list of services and contact details

Seminars
workshops
Coaching
podcasts

Daniel Porthwick
Health & Wellbeing Life Coach
0491 372 815
daniel@wovenpathwellness.example
wovenpathwellness.example

Industry/Entity Type

Life Coaching

Contact Information for Business Card

I like the use of colour from the logo to be used. I'm not a fan of white.

Requirements
Must have
• My tagline: The journey home starts with you
Nice to have
• Use of colour that is in the mind body soul logo

```html
<!DOCTYPE html>
<html lang="en">
<head>
<meta charset="utf-8">
<title>Woven Path Wellness – Business Card</title>
<link href="https://fonts.googleapis.com/css2?family=Open+Sans:ital,wght@0,400;0,600;0,700;1,400&display=swap" rel="stylesheet">
<style>
  :root {
    --stage: #1a1a1a;
    --coral: #f07268;
    --paper: #ffffff;
    --paper-warm: #fbfbfa;
    --ink: #4b4f52;
    --ink-soft: #7d858a;
    --mark: #8e5fb4;
    --white: #ffffff;
  }
  * { box-sizing: border-box; margin: 0; padding: 0; }
  html, body {
    width: 1200px; height: 1000px; overflow: hidden;
    background: var(--stage);
    font-family: "Open Sans", Arial, sans-serif;
  }
  .stage {
    position: relative; width: 1200px; height: 1000px;
    display: flex; align-items: center; justify-content: center; gap: 60px;
  }
  .card {
    position: relative; width: 520px; height: 300px;
    box-shadow: 0 10px 30px rgba(0,0,0,0.45);
  }

  /* Front */
  .card--front { background: var(--coral); padding: 15px; }
  .card__inner {
    width: 100%; height: 100%; background: var(--paper);
    display: flex; flex-direction: column; align-items: center; justify-content: center;
  }
  .brand__dot {
    width: 74px; height: 74px; border-radius: 50%;
    background: var(--mark); margin-bottom: 14px;
  }
  .brand__name {
    font-size: 26px; font-weight: 400; color: var(--ink-soft);
    letter-spacing: -0.5px; line-height: 1.1;
  }
  .brand__tagline {
    font-size: 13px; font-style: italic; color: var(--ink-soft);
    margin-top: 4px; letter-spacing: 0.3px;
  }

  /* Back */
  .card--back { background: var(--paper-warm); }
  .identity {
    position: absolute; left: 30px; top: 90px; width: 185px; text-align: right;
  }
  .identity__name { font-size: 17px; font-weight: 700; color: var(--coral); line-height: 1.3; }
  .identity__role { font-size: 14px; color: var(--ink); line-height: 1.4; }
  .divider {
    position: absolute; left: 230px; top: 82px; width: 1.5px; height: 78px; background: var(--ink);
  }
  .contact {
    position: absolute; left: 244px; top: 92px; list-style: none;
  }
  .contact__item {
    display: flex; align-items: center; gap: 7px;
    font-size: 14px; color: var(--ink); line-height: 21px;
  }
  .contact__icon { width: 11px; height: 11px; flex: none; fill: var(--coral); }
  .services {
    position: absolute; left: 14px; right: 50px; top: 206px; height: 44px;
    background: var(--coral); color: var(--white);
    display: flex; align-items: center; justify-content: space-around;
    font-size: 16px; list-style: none; padding: 0 10px;
  }
  .services__sep { opacity: 0.95; }
</style>
</head>
<body>
<main class="stage">
  <section class="card card--front" aria-label="Card front">
    <div class="card__inner">
      <span class="brand__dot" aria-hidden="true"></span>
      <p class="brand__name">Woven Path Wellness</p>
      <p class="brand__tagline">“the journey home starts with you ”</p>
    </div>
  </section>

  <section class="card card--back" aria-label="Card back">
    <div class="identity">
      <p class="identity__name">Daniel Porthwick</p>
      <p class="identity__role">Life Coach</p>
    </div>
    <span class="divider" aria-hidden="true"></span>
    <ul class="contact">
      <li class="contact__item">
        <svg class="contact__icon" viewBox="0 0 24 24" aria-hidden="true"><path d="M6.6 10.8a15.1 15.1 0 0 0 6.6 6.6l2.2-2.2a1 1 0 0 1 1-.25 11.4 11.4 0 0 0 3.6.57 1 1 0 0 1 1 1V20a1 1 0 0 1-1 1A17 17 0 0 1 3 4a1 1 0 0 1 1-1h3.5a1 1 0 0 1 1 1c0 1.25.2 2.45.57 3.6a1 1 0 0 1-.25 1z"/></svg>
        0491 372 815
      </li>
      <li class="contact__item">
        <svg class="contact__icon" viewBox="0 0 24 24" aria-hidden="true"><path d="M2 5h20v2l-10 6L2 7z M2 9l10 6 10-6v10H2z"/></svg>
        daniel@wovenpathwellness.example
      </li>
      <li class="contact__item">
        <svg class="contact__icon" viewBox="0 0 24 24" aria-hidden="true"><path d="M12 2a10 10 0 1 0 0 20 10 10 0 0 0 0-20zm6.9 6h-3a15.6 15.6 0 0 0-1.4-3.6A8 8 0 0 1 18.9 8zM12 4c.8 1.2 1.5 2.5 1.9 4h-3.8c.4-1.5 1.1-2.8 1.9-4zM4.3 14a8 8 0 0 1 0-4h3.4a16 16 0 0 0 0 4zm.8 2h3a15.6 15.6 0 0 0 1.4 3.6A8 8 0 0 1 5.1 16zm3-8h-3a8 8 0 0 1 4.4-3.6A15.6 15.6 0 0 0 8.1 8zM12 20c-.8-1.2-1.5-2.5-1.9-4h3.8c-.4 1.5-1.1 2.8-1.9 4zm2.3-6H9.7a14.7 14.7 0 0 1 0-4h4.6a14.7 14.7 0 0 1 0 4zm.2 5.6a15.6 15.6 0 0 0 1.4-3.6h3a8 8 0 0 1-4.4 3.6zm1.8-5.6a16 16 0 0 0 0-4h3.4a8 8 0 0 1 0 4z"/></svg>
        www.wovenpathwellness.example
      </li>
    </ul>
    <ul class="services">
      <li>Seminars</li><li class="services__sep" aria-hidden="true">/</li>
      <li>Workshops</li><li class="services__sep" aria-hidden="true">/</li>
      <li>Coaching</li><li class="services__sep" aria-hidden="true">/</li>
      <li>Podcasts</li>
    </ul>
  </section>
</main>
</body>
</html>
```